Looking for potential sellers

We help people buy and sell homes and are currently looking for potential home sellers. We offer low commissions, are the Local Colorado Springs and Falcon Experts, homes selling fast and at top dollar, Free expert pricing opinions and Consultations, over 9 years of experience, top rated Realtors creative and aggressive marketing strategies. Never merely own a house, THRIVE at Harborview. phone number 482-630-9157 web thriveatharborview.com

```html
<!DOCTYPE html>
<html lang="en">
<head>
<meta charset="utf-8">
<title>Harborline Realty – Seller Postcard</title>
<link rel="stylesheet" href="https://fonts.googleapis.com/css2?family=Montserrat:wght@500;700;800&family=Open+Sans:wght@400;600;700&family=Oswald:wght@500&display=swap">
<style>
  :root {
    --backdrop: #7a7a7a;
    --olive: #a6a83c;
    --olive-bright: #b9bb3f;
    --ink-dark: #2b2a18;
    --panel-dark: #1c1c1c;
    --paper: #ffffff;
    --stamp: #d2d2d2;
    --text-dark: #1f1f1f;
  }
  html, body {
    margin: 0;
    width: 1200px;
    height: 1200px;
    overflow: hidden;
    background: var(--backdrop);
  }
  .postcard {
    position: absolute;
    left: 211px;
    width: 758px;
    height: 513px;
    display: block;
  }
  .postcard--front { top: 79px; }
  .postcard--back { top: 614px; }
  .font-head { font-family: "Montserrat", sans-serif; }
  .font-body { font-family: "Open Sans", sans-serif; }
  .font-tagline { font-family: "Oswald", sans-serif; }
</style>
</head>
<body>

<!-- Front of the postcard -->
<svg class="postcard postcard--front" viewBox="0 0 948 641" xmlns="http://www.w3.org/2000/svg">
  <defs>
    <linearGradient id="frontPhoto" x1="0" y1="0" x2="0" y2="1">
      <stop offset="0" stop-color="#8fb9e6"/>
      <stop offset="0.45" stop-color="#b9c3c2"/>
      <stop offset="0.75" stop-color="#5d7a3f"/>
      <stop offset="1" stop-color="#3e5a2a"/>
    </linearGradient>
    <linearGradient id="portraitTone" x1="0" y1="0" x2="0" y2="1">
      <stop offset="0" stop-color="#cfc7c0"/>
      <stop offset="1" stop-color="#8d8580"/>
    </linearGradient>
  </defs>

  <rect class="card-base" width="948" height="641" fill="var(--paper)"/>

  <!-- header -->
  <polygon class="header-accent" points="242,0 262,0 306,111 948,111 948,129 292,129" fill="var(--olive)"/>
  <polygon class="header-brand-block" points="0,0 242,0 292,129 0,129" fill="var(--ink-dark)"/>
  <g class="brand-mark">
    <rect x="54" y="80" width="10" height="10" fill="var(--olive)"/>
    <text x="74" y="90" class="font-body" font-size="20" font-weight="600" fill="var(--paper)">Harborline Realty</text>
  </g>
  <text class="headline-lead font-head" x="317" y="47" font-size="30" font-weight="800" fill="var(--text-dark)">Are you currently looking for</text>
  <text class="headline-main font-head" x="317" y="89" font-size="38" font-weight="800" fill="var(--text-dark)" letter-spacing="1">POTENTIAL HOME  SELLERS ?</text>

  <!-- hero -->
  <rect class="hero-photo" x="0" y="129" width="948" height="362" fill="url(#frontPhoto)" role="img" aria-label="Two-storey craftsman house with landscaped front garden under a blue sky"/>

  <!-- agent bar -->
  <rect class="agent-bar" x="0" y="491" width="948" height="83" fill="var(--olive)"/>
  <rect class="url-bar" x="0" y="574" width="948" height="67" fill="var(--ink-dark)"/>

  <rect class="agent-portrait" x="24" y="414" width="139" height="153" rx="10" fill="url(#portraitTone)" stroke="var(--paper)" stroke-width="3" role="img" aria-label="Portrait photo of associate broker"/>
  <rect class="agent-portrait" x="782" y="414" width="139" height="153" rx="10" fill="url(#portraitTone)" stroke="var(--paper)" stroke-width="3" role="img" aria-label="Portrait photo of employing broker and owner"/>

  <g class="agent agent--left font-head" fill="var(--paper)">
    <text x="186" y="523" font-size="16" font-weight="800">CALEB MORROW</text>
    <text x="186" y="540" font-size="13" font-weight="500" letter-spacing="0.5">ASSOCIATE BROKER</text>
    <text x="186" y="561" font-size="12" font-weight="500" class="font-body">✆ 482-630-2264    ✆ 482-630-9157(office)</text>
  </g>
  <line class="agent-divider" x1="473" y1="512" x2="473" y2="564" stroke="var(--ink-dark)" stroke-width="3"/>
  <g class="agent agent--right font-head" fill="var(--paper)" text-anchor="end">
    <text x="761" y="523" font-size="16" font-weight="800">DEAN MORROW</text>
    <text x="761" y="540" font-size="13" font-weight="500" letter-spacing="0.5">EMPLOYING BROKER &amp; OWNER</text>
    <text x="761" y="561" font-size="12" font-weight="500" class="font-body">482-630-9157(office) ✆    482-630-9157 ✆</text>
  </g>

  <text class="site-url font-head" x="474" y="618" text-anchor="middle" font-size="22" font-weight="500" letter-spacing="6" fill="var(--paper)">www.thriveatharborview.com</text>
</svg>

<!-- Back of the postcard -->
<svg class="postcard postcard--back" viewBox="0 0 948 641" xmlns="http://www.w3.org/2000/svg">
  <defs>
    <linearGradient id="backPhoto" x1="0" y1="0" x2="0" y2="1">
      <stop offset="0" stop-color="#d9dde0"/>
      <stop offset="0.35" stop-color="#b4a968"/>
      <stop offset="0.75" stop-color="#9c9355"/>
      <stop offset="1" stop-color="#4f7a34"/>
    </linearGradient>
  </defs>

  <rect class="card-base" width="948" height="641" fill="var(--paper)"/>

  <polygon class="chevron-accent" points="396,0 438,0 541,308 481,641 0,641 0,0" fill="var(--olive)"/>
  <polygon class="hero-photo" points="0,0 396,0 535,308 0,308" fill="url(#backPhoto)" role="img" aria-label="Yellow family home with arched entry and flower beds"/>
  <polygon class="info-panel" points="0,308 535,308 462,578 0,578" fill="var(--panel-dark)"/>
  <polyline class="panel-edge" points="540,308 464,578" fill="none" stroke="var(--paper)" stroke-width="3"/>

  <text class="tagline font-tagline" x="27" y="344" font-size="25" font-weight="500" fill="var(--olive-bright)" textLength="430" lengthAdjust="spacingAndGlyphs">Never merely own a house, THRIVE at Harborview.</text>

  <g class="benefits font-body" fill="var(--paper)" font-size="16.5">
    <g class="benefit">
      <path d="M25 368 l3 3 l6 -7" stroke="var(--olive)" stroke-width="2" fill="none"/>
      <text x="45" y="375">Free expert pricing opinions and Consultations</text>
    </g>
    <g class="benefit">
      <path d="M25 399 l3 3 l6 -7" stroke="var(--olive)" stroke-width="2" fill="none"/>
      <text x="45" y="406">Over 9 years of experience</text>
    </g>
    <g class="benefit">
      <path d="M25 430 l3 3 l6 -7" stroke="var(--olive)" stroke-width="2" fill="none"/>
      <text x="45" y="437">Top rated Realtors creative</text>
    </g>
    <g class="benefit">
      <path d="M25 462 l3 3 l6 -7" stroke="var(--olive)" stroke-width="2" fill="none"/>
      <text x="45" y="469">Aggressive marketing strategies</text>
    </g>
  </g>

  <g class="call-to-action">
    <rect x="24" y="493" width="411" height="74" rx="37" fill="none" stroke="var(--olive)" stroke-width="1.5"/>
    <text class="font-body" x="228" y="518" text-anchor="middle" font-size="15" font-weight="700" fill="var(--paper)">FOR MORE DETAILS PLEASE  CALL US TODAY</text>
    <g class="phone-icon" transform="translate(119 545)">
      <circle r="9" fill="none" stroke="var(--paper)" stroke-width="1.5"/>
      <path d="M-4 -4 q0 8 8 8 l1 -2 l-2 -2 l-2 1 q-3 -1 -4 -4 l1 -2 l-2 -2 z" fill="var(--paper)"/>
    </g>
    <text class="font-body" x="140" y="554" font-size="25" font-weight="700" fill="var(--paper)">482-630-9157</text>
  </g>

  <text class="site-url font-body" x="228" y="620" text-anchor="middle" font-size="20" letter-spacing="3" fill="var(--paper)">www.thriveatharborview.com</text>

  <!-- mailing side -->
  <g class="brand-mark">
    <rect x="494" y="70" width="9" height="9" fill="var(--text-dark)"/>
    <text x="510" y="79" class="font-body" font-size="17" font-weight="600" fill="var(--text-dark)">Harborline Realty</text>
  </g>
  <rect class="stamp-box" x="844" y="25" width="73" height="83" fill="var(--stamp)"/>
  <g class="address-lines" stroke="var(--text-dark)" stroke-width="1.2">
    <line x1="689" y1="305" x2="917" y2="305"/>
    <line x1="689" y1="341" x2="917" y2="341"/>
    <line x1="689" y1="378" x2="917" y2="378"/>
  </g>
</svg>

</body>
</html>
```